Business Card Design To Look Just Like a Credit Card- Needed

I would like to take my new Logo just designed here at Pixel Harbor and make a new business card and template for future additional sales people.
The credit card should have an eye catching design but look real. I have seen some that have similar logos to LORU or TrustPlaque too. However,it must have a smart chip design in it too. Make sure it has a black fake magnetic strip and other characteristics of an actual modern credit card.
This may be printed on paper and blank plastic cards.

Most the information will be on the back but the name will be on front with the logo, phone number.

Must Have Info:
Leonard Whitfield
President

2964 Maple Hollow Rd, Bldg 417
Fairport, NY 14582
252-555-0187
leonard@brightledgerco.net
Updates

Phone number is 585 area code not 252! my bad

also, please add website address www.brightledgerco.net
Thanks,

LW

Industry/Entity Type

Credit Card

Requirements
Must have
• My Logo, smart chip, fake magnetic strip

```html
<!DOCTYPE html>
<html lang="en">
<head>
<meta charset="utf-8">
<title>Bright Ledger – Leonard Whitfield Business Card</title>
<link rel="stylesheet" href="https://fonts.googleapis.com/css2?family=Archivo:wght@400;700&family=Share+Tech+Mono&display=swap">
<style>
  :root {
    --card-black: #1c1e1b;
    --page-white: #ffffff;
    --brand-green: #1d7a34;
    --map-green: #5f9e2a;
    --map-lime: #9cc22a;
    --map-yellow: #f2ea16;
    --chip-gold: #f3bd3c;
    --chip-light: #fde7a1;
    --chip-line: #b98417;
    --emboss-silver: #d9dbdc;
    --label-white: #f4f4f4;
  }
  * { box-sizing: border-box; margin: 0; padding: 0; }
  html, body {
    width: 1200px;
    height: 762px;
    overflow: hidden;
    background: var(--page-white);
  }
  .card {
    position: relative;
    width: 1200px;
    height: 762px;
    background: var(--card-black);
    border-radius: 30px;
    overflow: hidden;
    font-family: "Archivo", Arial, sans-serif;
  }
  .brand-name {
    position: absolute;
    left: 34px;
    top: 150px;
    color: var(--brand-green);
    font-family: "Archivo", Arial, sans-serif;
    font-weight: 700;
    font-size: 46px;
    line-height: 44px;
    letter-spacing: 0.5px;
  }
  .world-map {
    position: absolute;
    left: 338px;
    top: 128px;
    width: 847px;
    height: 500px;
    border-radius: 40px;
    background: linear-gradient(90deg, var(--map-green) 0%, var(--map-lime) 35%, var(--map-yellow) 62%, var(--map-yellow) 100%);
    opacity: 0.55;
  }
  .card-arrow {
    position: absolute;
    left: 0;
    top: 306px;
  }
  .smart-chip {
    position: absolute;
    left: 117px;
    top: 312px;
  }
  .card-number {
    position: absolute;
    left: 114px;
    top: 492px;
    font-family: "Share Tech Mono", "Courier New", monospace;
    font-size: 72px;
    letter-spacing: 9px;
    color: var(--emboss-silver);
    text-shadow: 2px 2px 0 #6f7273, -1px -1px 0 #ffffff;
    white-space: pre;
  }
  .holder {
    position: absolute;
    left: 117px;
    top: 636px;
    font-family: "Share Tech Mono", "Courier New", monospace;
    font-size: 38px;
    letter-spacing: 5px;
    line-height: 42px;
    color: var(--emboss-silver);
    text-shadow: 1px 1px 0 #6f7273;
    text-align: center;
  }
  .validity {
    position: absolute;
    top: 608px;
    color: var(--label-white);
    text-align: center;
  }
  .validity-label {
    font-size: 16px;
    font-weight: 400;
    letter-spacing: 0.3px;
  }
  .validity-from { left: 686px; }
  .validity-from .validity-date {
    font-family: "Share Tech Mono", "Courier New", monospace;
    font-size: 40px;
    letter-spacing: 4px;
    color: var(--emboss-silver);
    margin-top: 12px;
  }
  .validity-to { left: 915px; }
  .validity-to .validity-date {
    font-size: 30px;
    margin-top: 18px;
  }
</style>
</head>
<body>
<main class="card">
  <div class="brand-name">BRIGHT<br>LEDGER</div>

  <div class="world-map" role="img" aria-label="Dotted world map in green fading to yellow"></div>

  <svg class="card-arrow" width="70" height="172" viewBox="0 0 70 172" aria-hidden="true">
    <defs>
      <linearGradient id="arrowFill" x1="0" y1="0" x2="1" y2="0">
        <stop offset="0" stop-color="#f4e81a"/>
        <stop offset="1" stop-color="#7fae22"/>
      </linearGradient>
    </defs>
    <polygon points="4,86 66,2 66,170" fill="url(#arrowFill)"/>
  </svg>

  <svg class="smart-chip" width="166" height="157" viewBox="0 0 166 157" aria-hidden="true">
    <defs>
      <linearGradient id="chipFill" x1="0" y1="0" x2="0" y2="1">
        <stop offset="0" stop-color="var(--chip-light)"/>
        <stop offset="0.45" stop-color="var(--chip-gold)"/>
        <stop offset="1" stop-color="#e0a22b"/>
      </linearGradient>
    </defs>
    <rect x="1" y="1" width="164" height="155" rx="24" fill="url(#chipFill)" stroke="var(--chip-line)" stroke-width="2"/>
    <g fill="none" stroke="var(--chip-line)" stroke-width="3">
      <path d="M1 52 H46 M1 104 H46 M120 52 H165 M120 104 H165"/>
      <path d="M62 1 V34 M104 1 V34 M62 156 V122 M104 156 V122"/>
      <rect x="46" y="34" width="74" height="88" rx="14"/>
    </g>
  </svg>

  <div class="card-number">1234 5678 9101 1213</div>

  <div class="holder">
    <div class="holder-name">LEONARD WHITFIELD</div>
    <div class="holder-title">(PRESIDENT)</div>
  </div>

  <div class="validity validity-from">
    <div class="validity-label">VALID FIRST DAY OF</div>
    <div class="validity-date">01/13</div>
  </div>
  <div class="validity validity-to">
    <div class="validity-label">TO LAST DAY OF</div>
    <div class="validity-date">01/14</div>
  </div>
</main>
</body>
</html>
```